Ecard for facebook and Instagram postings

I need 4 ecards (don't know if that is what it is called) for Facebook and Instagram postings. My Logo and company name should be incorporated and also be square. I would like to be able to insert text as I need. Examples are:

https://www.pinwheelsocial.example/photo.php?fbid=20284619375028461&set=a.20273946105827394.718352.94735186024&type=1&relevant_count=1

https://media-b-ord.xx.tilecdnhub.example/pics-lke7/8765432_135792468013579_864209753_n.jpg

I don't necessarily need images on them, just the color scheme to my business cards and the logo and business name. But if you'd like to give it an interesting look, you can go ahead and play with it. My site is sunmeadowcoaching.example, if you'd like to see the style of it.

Thank you!!!
Updates

I just uploaded the logo in two variations.  Thank you!

Target Market(s)

Women 16-65

Industry/Entity Type

Business

Requirements
Must have
• Logo and business name
Should not have
• No white background. I have attached business card picture so you can have an idea of what I'd like.

```html
<!DOCTYPE html>
<html lang="en">
<head>
<meta charset="utf-8">
<title>Sun Meadow Coaching Services – Social Card</title>
<link rel="stylesheet" href="https://fonts.googleapis.com/css2?family=Roboto+Condensed:wght@700&display=swap">
<style>
  :root {
    --orange-deep: #ef8226;
    --orange-mid: #f6ad62;
    --peach-light: #fde9cd;
    --cream: #fffaf2;
    --band-top: #fcdcae;
    --band-bottom: #f39a3f;
    --brand-red: #b8182e;
    --rule-red: #c6202f;
    --ring: rgba(240, 190, 170, 0.45);
  }
  * { margin: 0; padding: 0; box-sizing: border-box; }
  html, body {
    width: 1200px;
    height: 1196px;
    overflow: hidden;
    background: var(--cream);
  }
  .social-card {
    position: relative;
    width: 1200px;
    height: 1196px;
    overflow: hidden;
    background:
      radial-gradient(ellipse 900px 700px at 180px 1020px, var(--cream) 0%, rgba(255,250,242,0.85) 30%, rgba(255,250,242,0) 75%),
      linear-gradient(160deg, var(--orange-deep) 0%, var(--orange-mid) 35%, var(--peach-light) 70%, var(--cream) 100%);
  }
  .decor-ring {
    position: absolute;
    left: 0;
    top: 0;
  }
  .footer-band {
    position: absolute;
    left: 0;
    top: 1018px;
    width: 1200px;
    height: 178px;
    background: linear-gradient(180deg, var(--band-top) 0%, var(--orange-mid) 55%, var(--band-bottom) 100%);
    border-top: 5px solid var(--rule-red);
  }
  .footer-band::after {
    content: "";
    position: absolute;
    left: 0;
    bottom: 0;
    width: 100%;
    height: 12px;
    background: var(--rule-red);
  }
  .site-address {
    position: absolute;
    left: 26px;
    top: 1100px;
    font-family: "Roboto Condensed", sans-serif;
    font-weight: 700;
    font-size: 32px;
    color: var(--brand-red);
    letter-spacing: 0.2px;
  }
  .brand-mark {
    position: absolute;
    left: 850px;
    top: 935px;
    width: 330px;
    text-align: center;
  }
  .brand-dot {
    display: block;
    width: 96px;
    height: 96px;
    margin: 0 auto;
    border-radius: 50%;
    background: var(--orange-deep);
    border: 6px solid #ffffff;
  }
  .brand-name {
    display: block;
    margin-top: 12px;
    font-family: "Roboto Condensed", sans-serif;
    font-weight: 700;
    font-size: 50px;
    line-height: 1;
    color: var(--brand-red);
  }
  .brand-tagline {
    display: block;
    margin-top: 10px;
    font-family: "Roboto Condensed", sans-serif;
    font-weight: 700;
    font-size: 22px;
    letter-spacing: 4px;
    color: var(--brand-red);
  }
</style>
</head>
<body>
  <main class="social-card">
    <svg class="decor-ring" width="1200" height="1196" viewBox="0 0 1200 1196" aria-hidden="true">
      <circle cx="905" cy="690" r="305" fill="none" stroke="var(--ring)" stroke-width="7"/>
    </svg>

    <footer class="footer-band"></footer>

    <p class="site-address">www.sunmeadowcoaching.example</p>

    <div class="brand-mark">
      <span class="brand-dot"></span>
      <span class="brand-name">Sun Meadow</span>
      <span class="brand-tagline">COACHING SERVICES</span>
    </div>
  </main>
</body>
</html>
```